Sales Page Header Design Project

Hi,
I need a background image created for this sales page: http://corvellatrainingcamp.com
Width: 977 px
Height: 150 px
Here are a few sample designs to work with: http://mintwaterstudiohall.com/
http://paintingthefenceweb.com/wp-content/uploads/2011/02/experts1.png
Must be sharp, professional looking and uncluttered.
Colours: Must include blue (I like the blue on the on the current sales page, but will leave shade and colour combinations to your creativity)
Text = Tobi Marvenko Presents
Corvella Training Camp
Your Blueprint for Building a Profitable, Sustainable Business in Today's Economy!
Any questions, give me a shout
Entrepreneurs and Business Owners, aged 21 to 45
Business

```html
<!DOCTYPE html>
<html lang="en">
<head>
<meta charset="utf-8">
<title>Corvella Training Camp – Header</title>
<link rel="stylesheet" href="https://fonts.googleapis.com/css2?family=Cinzel:wght@400;500&family=Didact+Gothic&display=swap">
<style>
  :root {
    --stage: #211816;
    --blue-edge: #3e86cf;
    --blue-mid: #a9c6ea;
    --white: #ffffff;
    --title-ink: #2f2f2f;
    --small-ink: #1d1d1d;
    --piece-orange: #e0762d;
    --piece-pink: #cf3f93;
    --piece-purple: #5a4a9e;
    --piece-teal: #3e9a8c;
    --piece-green: #8ab13c;
  }
  * { margin: 0; padding: 0; box-sizing: border-box; }
  html, body {
    width: 1200px;
    height: 900px;
    overflow: hidden;
    background: var(--stage);
  }
  .canvas {
    position: relative;
    width: 1200px;
    height: 900px;
  }
  .header-banner {
    position: absolute;
    left: 70px;
    top: 161px;
    width: 1050px;
    height: 162px;
    background: linear-gradient(90deg,
      var(--blue-edge) 0%,
      var(--blue-mid) 14%,
      var(--white) 26%,
      var(--white) 74%,
      var(--blue-mid) 86%,
      var(--blue-edge) 100%);
    overflow: hidden;
  }
  .puzzle-art {
    position: absolute;
    top: 54px;
    height: 66px;
    border-radius: 8px;
  }
  .puzzle-art.left {
    left: 76px;
    width: 180px;
    background: linear-gradient(90deg, var(--piece-orange) 0%, var(--piece-pink) 50%, var(--piece-purple) 100%);
  }
  .puzzle-art.right {
    left: 802px;
    width: 180px;
    background: linear-gradient(90deg, var(--piece-purple) 0%, var(--piece-teal) 50%, var(--piece-green) 100%);
  }
  .presenter {
    position: absolute;
    left: 283px;
    top: 40px;
    font-family: "Didact Gothic", sans-serif;
    font-size: 13px;
    line-height: 16px;
    color: var(--small-ink);
    letter-spacing: 0.2px;
    white-space: nowrap;
  }
  .event-title,
  .event-title-reflection {
    position: absolute;
    left: 277px;
    top: 53px;
    height: 45px;
    font-family: "Cinzel", serif;
    font-weight: 400;
    font-size: 45px;
    line-height: 45px;
    color: var(--title-ink);
    white-space: nowrap;
    letter-spacing: 0.5px;
  }
  .event-title .cap-small,
  .event-title-reflection .cap-small { font-size: 34px; }
  .event-title { z-index: 2; }
  .event-title-reflection {
    z-index: 0;
    transform-origin: 0 36px;
    transform: scaleY(-0.5);
    opacity: 0.22;
    -webkit-mask-image: linear-gradient(to top, rgba(0,0,0,1) 30%, rgba(0,0,0,0) 80%);
    mask-image: linear-gradient(to top, rgba(0,0,0,1) 30%, rgba(0,0,0,0) 80%);
  }
  .tagline {
    position: absolute;
    z-index: 3;
    left: 280px;
    top: 103px;
    font-family: "Didact Gothic", sans-serif;
    font-size: 14px;
    line-height: 18px;
    color: var(--small-ink);
    white-space: nowrap;
  }
</style>
</head>
<body>
  <main class="canvas">
    <header class="header-banner">
      <div class="puzzle-art left" role="img" aria-label="Three interlocking puzzle pieces in orange, pink and purple with chart, question mark and cursor icons"></div>
      <p class="presenter">Tobi Marvenko Presents</p>
      <div class="event-title-reflection" aria-hidden="true">C<span class="cap-small">ORVELLA</span> T<span class="cap-small">RAINING</span> C<span class="cap-small">AMP</span></div>
      <h1 class="event-title">C<span class="cap-small">ORVELLA</span> T<span class="cap-small">RAINING</span> C<span class="cap-small">AMP</span></h1>
      <p class="tagline">Your Blueprint for Building a Profitable, Sustainable Business in Today's Economy!</p>
      <div class="puzzle-art right" role="img" aria-label="Three interlocking puzzle pieces in purple, teal and green with cursor, dollar sign and world icons"></div>
    </header>
  </main>
</body>
</html>
```